Super elegant, crisp & clean Business card design required

We recently upgraded our branding - which is on our website - tavorelstudio.com

I would like a simple, yet elegant, clean business card design please.

The font of my logo is Cinzel - and because of the natural colour - it's best to have this on a black background.

I would like to have the back of the business card - with simply my logo.

PLEASE DO NOT SUBMIT A COMPLICATED / UNCLEAN DESIGN

Industry/Entity Type

Business

Contact Information for Business Card

Dalvik Ostrander Photography

Font styles to use
Other font styles liked:
• Cinzel

Requirements
Must have
• A backpage with nothing but my logo
• Simple design - stands out
Should not have
• Colour that dont align with my logo
• Over complicated '/ non symmetrical design

```html
<!DOCTYPE html>
<html lang="en">
<head>
<meta charset="utf-8">
<title>Dalvik Ostrander Photography – Business Card</title>
<link rel="stylesheet" href="https://fonts.googleapis.com/css2?family=Cinzel:wght@400&family=Roboto:wght@400;500&display=swap">
<style>
  :root {
    --page: #e9e6e1;
    --card-top: #353536;
    --card-bottom: #262627;
    --gold: #b6a684;
    --gold-soft: #9d8f74;
    --text-muted: #c9c3b6;
    --icon-dark: #2b2b2c;
  }
  * { margin: 0; padding: 0; box-sizing: border-box; }
  html, body { width: 1200px; height: 1023px; overflow: hidden; background: var(--page); }
  .sheet {
    width: 1200px; height: 1023px;
    display: flex; flex-direction: column; align-items: center; justify-content: center; gap: 56px;
  }
  .card {
    position: relative;
    width: 640px; height: 366px;
    border-radius: 22px;
    background: linear-gradient(160deg, var(--card-top), var(--card-bottom));
    box-shadow: 0 10px 24px rgba(0,0,0,0.25);
    overflow: hidden;
  }
  /* Front */
  .identity { position: absolute; left: 48px; top: 56px; font-family: "Roboto", sans-serif; }
  .identity-name { color: var(--gold); font-size: 27px; font-weight: 500; letter-spacing: 0.2px; }
  .identity-role { color: var(--gold-soft); font-size: 16px; margin-top: 4px; }
  .contact { position: absolute; left: 0; bottom: 44px; display: flex; align-items: stretch; }
  .contact-tab {
    width: 38px; background: var(--gold);
    display: flex; flex-direction: column; justify-content: space-around; align-items: center;
    padding: 6px 0;
  }
  .contact-tab svg { width: 15px; height: 15px; }
  .contact-list {
    list-style: none; padding-left: 14px;
    font-family: "Roboto", sans-serif; font-size: 16px; color: var(--text-muted);
    display: flex; flex-direction: column; gap: 9px; justify-content: center;
  }
  .front-mark {
    position: absolute; right: 52px; top: 50%; transform: translateY(-50%);
    display: flex; align-items: center; gap: 12px;
    font-family: "Cinzel", serif; font-size: 22px; color: var(--gold); letter-spacing: 1px;
  }
  .mark-dot { width: 14px; height: 14px; border: 1.5px solid var(--gold); border-radius: 50%; }
  /* Back */
  .back-mark {
    position: absolute; inset: 0;
    display: flex; flex-direction: column; align-items: center; justify-content: center; gap: 14px;
    font-family: "Cinzel", serif; color: var(--gold-soft); text-align: center;
  }
  .back-mark-circle { width: 18px; height: 18px; border: 1.5px solid var(--gold-soft); border-radius: 50%; }
  .back-mark-name { font-size: 38px; letter-spacing: 1px; line-height: 1.25; }
  .back-mark-name span { display: block; font-size: 38px; letter-spacing: 12px; }
</style>
</head>
<body>
<main class="sheet">
  <section class="card card-front" aria-label="Business card front">
    <div class="identity">
      <p class="identity-name">Dalvik Ostrander</p>
      <p class="identity-role">Photographer</p>
    </div>
    <div class="contact">
      <div class="contact-tab">
        <svg viewBox="0 0 16 16" aria-hidden="true"><path fill="var(--icon-dark)" d="M3.6 1.5l2.3 2.6-1.3 1.7c.9 2 2.5 3.6 4.5 4.5l1.7-1.3 2.6 2.3-1.3 2.1C7.3 13.2 2.8 8.7 1.5 3z"/></svg>
        <svg viewBox="0 0 16 16" aria-hidden="true"><rect x="1.5" y="3.5" width="13" height="9" fill="none" stroke="var(--icon-dark)" stroke-width="1.4"/><path d="M1.5 3.5l6.5 5 6.5-5" fill="none" stroke="var(--icon-dark)" stroke-width="1.4"/></svg>
        <svg viewBox="0 0 16 16" aria-hidden="true"><g fill="none" stroke="var(--icon-dark)" stroke-width="1.3"><circle cx="8" cy="8" r="6.3"/><ellipse cx="8" cy="8" rx="2.8" ry="6.3"/><path d="M1.7 8h12.6M2.8 4.8h10.4M2.8 11.2h10.4"/></g></svg>
      </div>
      <ul class="contact-list">
        <li>07940218653</li>
        <li>hello@tavorelstudio.com</li>
        <li>tavorelstudio.com</li>
      </ul>
    </div>
    <div class="front-mark">
      <span class="mark-dot" aria-hidden="true"></span>
      <span>Dalvik Ostrander</span>
    </div>
  </section>

  <section class="card card-back" aria-label="Business card back">
    <div class="back-mark">
      <span class="back-mark-circle" aria-hidden="true"></span>
      <p class="back-mark-name">DALVIK OSTRANDER<span>PHOTOGRAPHY</span></p>
    </div>
  </section>
</main>
</body>
</html>
```